Fun/Happy Business Card & New Logo for Home Cake Shop

We need a business card for a small home-based, 2 person husband/wife bakery where we do cakes, cupcakes, eclairs, cream puffs and such. Our company name is Plum Crumb Bakehouse.

We generally like the colour pink, but are open to other colour scheme ideas as well. The head chef(wife) is a very fun-loving, always cheerful and happy person and we want the business card to reflect her bubbly personality.

The business card should contain the husband's name AND the wife's name.
Updates

1st place prize money has been increased as requested. Thanks for your designs so far! 

Target Market(s)

Generally adults, for birthdays or small/medium sized catering events.

Industry/Entity Type

Bakery

Requirements
Must have
• Name 1: Soraya Pettit
Phone: 93816275

Name 2: Marcel Pettit
Phone: 96214853

Email: info@plumcrumbbakehouse.com
Website: www.plumcrumbbakehouse.com

Additional Info, Edit: Please ensure that the logo contains a cake and at least a couple cupcakes.
Nice to have
• I have uploaded a couple images with the general feel of what we want. The logo should be one with a cake and some cupcakes around it, with the words Plum Crumb Bakehouse. Try to come up with something more impressive than the current logo we have.

For the draft name card I uploaded in the file, that is also what we're sort of looking at. Try to come up with something more impressive/creative than that name card as well.

For the back of the name card, we are happy with just having the logo there. We're not sure what colour scheme would go best just yet, so feel free to show us your creative minds! :)

Additional Info, Edit: Please try to come up with a more realistic type of cake and cupcakes in the logo. We do not want it to be too cartoony. The attached images are just examples of the format.
Should not have
• Wordings or images that indicate 'Phone', 'Email' or 'Website' do not need to be included. Our customer base should be able to identify what an email and a website looks like. However, if you find that it looks particularly better, then feel free to be creative.

```html
<!DOCTYPE html>
<html lang="en">
<head>
<meta charset="utf-8">
<title>Plum Crumb Bakehouse – Business Card</title>
<link href="https://fonts.googleapis.com/css2?family=Nunito:wght@800&display=swap" rel="stylesheet">
<style>
  :root {
    --backdrop: #2e2e2e;
    --card: #ffffff;
    --ink: #5a5a5a;
    --pink: #f3b9c6;
    --pink-soft: #f6ccd5;
    --sky: #bfe3ee;
    --teal: #4aa9bf;
    --plum: #b468b4;
  }
  * { margin: 0; padding: 0; box-sizing: border-box; }
  html, body {
    width: 1200px; height: 900px; overflow: hidden;
    background: var(--backdrop);
    font-family: "Nunito", "Arial Rounded MT Bold", sans-serif;
    font-weight: 800;
  }
  .stage {
    position: relative; width: 1200px; height: 900px;
    display: flex; flex-direction: column; align-items: center; justify-content: center; gap: 56px;
  }
  .card {
    position: relative; width: 620px; height: 354px;
    background: var(--card); overflow: hidden;
  }

  /* Back of card */
  .card-back .cupcake-row {
    position: absolute; left: 0; right: 0; top: 110px; height: 56px;
    background: linear-gradient(90deg, var(--pink-soft), var(--sky), var(--pink-soft), var(--pink-soft), var(--sky), var(--pink-soft), var(--sky));
    opacity: .8;
  }
  .card-back .wordmark {
    position: absolute; left: 270px; top: 180px;
    color: var(--plum); font-size: 30px; letter-spacing: .2px;
  }

  /* Front of card */
  .card-front .cupcake-panel {
    position: absolute; left: 0; top: 0; bottom: 0; width: 160px;
  }
  .card-front .cupcake-shape {
    position: absolute; left: 0; top: 0; bottom: 0; width: 150px;
    background: var(--pink);
    border-top-right-radius: 40px;
    box-shadow: 7px 0 0 var(--sky);
  }
  .card-front .wordmark-vertical {
    position: absolute; left: 52px; bottom: 22px;
    transform-origin: left bottom; transform: rotate(-90deg) translateY(100%);
    color: var(--ink); font-size: 27px; white-space: nowrap;
  }
  .card-front .contacts {
    position: absolute; left: 250px; width: 300px; top: 52px;
    text-align: center; color: var(--ink); font-size: 22px; line-height: 1.2;
  }
  .card-front .divider-cake {
    width: 34px; height: 28px; margin: 6px auto 4px;
    background: var(--teal); border-radius: 14px 14px 4px 4px;
  }
  .card-front .web {
    position: absolute; left: 186px; top: 262px;
    color: var(--ink); font-size: 20px; line-height: 1.75;
  }
</style>
</head>
<body>
<main class="stage">
  <section class="card card-back" aria-label="Back of business card">
    <div class="cupcake-row" role="img" aria-label="Row of pink and light blue cupcake silhouettes"></div>
    <p class="wordmark">Plum Crumb Bakehouse</p>
  </section>

  <section class="card card-front" aria-label="Front of business card">
    <div class="cupcake-panel">
      <div class="cupcake-shape" role="img" aria-label="Large pink cupcake silhouette with light blue outline"></div>
      <p class="wordmark-vertical">Plum Crumb Bakehouse</p>
    </div>
    <div class="contacts">
      <p>Marcel Pettit</p>
      <p>Phone: 96214853</p>
      <div class="divider-cake" role="img" aria-label="Small teal cupcake silhouette"></div>
      <p>Soraya Pettit</p>
      <p>Phone: 93816275</p>
    </div>
    <div class="web">
      <p>info@plumcrumbbakehouse.com</p>
      <p>www.plumcrumbbakehouse.com</p>
    </div>
  </section>
</main>
</body>
</html>
```